"Copper Horizons" poster for feature film

I need a poster for my first narrative feature film. Genre: Drama/Comedy. Synopsis: After going through a break up and moving back home, Tobias struggles through a "quarter life crisis" in pursuit of his dream of making a feature film. Tobias wants to tell a compassionate story about mental illness and its effects on a family, but the lines between fiction and reality are blurred, challenging the bond between two brothers.

Target Market(s)

Film Festivals, Prospective viewers on Vidorly/Quorvia.

Industry/Entity Type

Film Production

Other font styles liked:
• Birch STD

Colors
faa54b
f78f20
85abd2
3176b5
0355a3
fac994
f9ba93
f37122
fece3e

Requirements
Must have
• Title: Copper Horizons
• Minimalist approach.
• Please look at reference posters/prototypes.
Nice to have
• -the idea of contrasting the two brothers and the struggle of living with a mental illness.
• -the setting of the film is in Arizona, desert, living back at home as an adult.
• -the struggle of a writer. A film about a film.
• 5 phases of "The Quarter Life Crisis"
• 1. You feel trapped by your life choices, like your job, relationship, or both. You’re living on “autopilot.”
• 2. You get a sense of “I’ve got to get out of this” and feel a growing sense that change is possible if you just take a leap.
• 3. You quit the job, end the relationship, or break the commitment that’s making you feel trapped. Then you detach and enter a “time out” period where try to rediscover who you are and who you want to be.
• 4. You begin rebuilding your life slowly but surely.
• 5. You develop new commitments that are more in line with your interests and aspirations.

```html
<!DOCTYPE html>
<html lang="en">
<head>
<meta charset="utf-8">
<title>Copper Horizons — Poster</title>
<link rel="stylesheet" href="https://fonts.googleapis.com/css2?family=Oranienbaum&family=Oswald:wght@300;400&display=swap">
<style>
  :root {
    --backdrop: #ececec;
    --paper: #ffffff;
    --ink: #0d0f24;
    --credit-grey: #7a7a7a;
    --sky-navy: #1c1f38;
    --dusk-blue: #3a3f5c;
    --horizon-glow: #f7b27a;
    --horizon-orange: #f37122;
    --ground-black: #0a0a0c;
  }
  * { margin: 0; padding: 0; box-sizing: border-box; }
  html, body {
    width: 1200px; height: 1200px; overflow: hidden;
    background: var(--backdrop);
  }
  .poster {
    position: absolute; left: 200px; top: 0;
    width: 800px; height: 1200px;
    background: var(--paper);
  }
  .key-art {
    position: absolute; left: 100px; top: 72px;
    width: 600px; height: 760px;
  }
  .tagline {
    position: absolute; left: 0; width: 100%;
    text-align: center;
    font-family: "Oranienbaum", serif;
    color: var(--ink);
  }
  .tagline--question { top: 836px; font-size: 30px; }
  .tagline--answer { top: 870px; font-size: 23px; }
  .title {
    position: absolute; left: 0; width: 100%; top: 888px;
    text-align: center;
    font-family: "Oranienbaum", serif;
    font-size: 124px; line-height: 1;
    color: var(--ink);
    letter-spacing: -1px;
  }
  .credits {
    position: absolute; left: 0; width: 100%; top: 1042px;
    text-align: center;
    font-family: "Oswald", sans-serif;
    font-weight: 400;
    font-size: 11.5px;
    line-height: 18px;
    color: var(--credit-grey);
    text-transform: uppercase;
  }
  .credits__label {
    font-size: 5px; line-height: 1;
    display: inline-block; width: 18px;
    vertical-align: middle; margin: 0 2px;
    font-weight: 300;
  }
</style>
</head>
<body>
  <main class="poster">
    <svg class="key-art" viewBox="0 0 600 760" role="img"
         aria-label="Symmetrical ink-blot silhouette with pink, yellow and blue paint splashes, framing a desert dusk scene of two brothers sitting by a campfire">
      <defs>
        <linearGradient id="dusk" x1="0" y1="0" x2="0" y2="1">
          <stop offset="0" stop-color="var(--sky-navy)"/>
          <stop offset="0.5" stop-color="var(--dusk-blue)"/>
          <stop offset="0.62" stop-color="var(--horizon-glow)"/>
          <stop offset="0.68" stop-color="var(--horizon-orange)"/>
          <stop offset="0.74" stop-color="var(--ground-black)"/>
          <stop offset="1" stop-color="var(--ground-black)"/>
        </linearGradient>
      </defs>
      <path fill="url(#dusk)"
            d="M300 40 C360 40 420 60 470 110 C520 170 520 260 510 330
               C520 400 530 460 560 500 C600 530 600 560 560 570
               C520 600 510 650 470 700 C430 740 370 720 300 740
               C230 720 170 740 130 700 C90 650 80 600 40 570
               C0 560 0 530 40 500 C70 460 80 400 90 330
               C80 260 80 170 130 110 C180 60 240 40 300 40 Z"/>
    </svg>

    <p class="tagline tagline--question">You wanna be a filmmaker?</p>
    <p class="tagline tagline--answer">Be the coyote</p>

    <h1 class="title">Copper Horizons</h1>

    <div class="credits">
      <p>Studio Name Pictures <span class="credits__label">presents a</span> Producers <span class="credits__label">a film by</span> Script Writer Actor One Actor Two "Movie Title"</p>
      <p><span class="credits__label">music by</span> The Musician <span class="credits__label">costume designer</span> Designer Name <span class="credits__label">edited by</span> Editors Name <span class="credits__label">production designer</span> Designers Name <span class="credits__label">director of photography</span> Cinematographer</p>
      <p><span class="credits__label">executive producer</span> Ex Producer 1 Ex Producer 2 <span class="credits__label">produced by</span> Producer One Producer 2 <span class="credits__label">story by</span> Story Writer</p>
      <p><span class="credits__label">screenplay by</span> Screen Writer <span class="credits__label">directed by</span> Director Name</p>
    </div>
  </main>
</body>
</html>
```